Lebel for 500g Honey Jar

We want a design for a 500g honey bottle or Jar as shown in the attached image . All Requirement has been put in the attached brief document .
Also Logo and images have been uploaded . Feel free to play arround with the selected solor schemes .

Target Market(s)

Retail Market

Industry/Entity Type

FMCG

Colors
00AB8E
00BBA5
67D7C9
C6EFE9
E9F9F6
59FF00
82FF00
B8FF75
E3FFCB
F4FFEA
FFC000
F8CF3A
FAE287
FDF2CF
FEFAEE
F0912C
F2A743
F7CA91
FBE8D2
FDF5EE
EE7325
F08F49
F5BC92
FAE3D3
FDF4ED

Requirements
Must have
• The desing must contain the company Address, Logo , and Nutritional Facts
Nice to have
• Image of a honey Bee , see samples attahed

```html
<!DOCTYPE html>
<html lang="en">
<head>
<meta charset="utf-8">
<title>Pure Honey Label 500g</title>
<link rel="stylesheet" href="https://fonts.googleapis.com/css2?family=Shrikhand&family=Gochi+Hand&family=Montserrat:wght@500;600;700&display=swap">
<style>
  :root {
    --page-bg: #eef0f1;
    --border-green: #0f6a3a;
    --label-cream: #fffdf4;
    --label-warm: #fdf2cf;
    --honey-gold: #ffc000;
    --honey-light: #fae287;
    --honey-orange: #f0912c;
    --honey-deep: #ee7325;
    --title-brown: #7a3d12;
    --claim-red: #ee4b25;
    --farm-green: #1f7a3f;
    --ink: #2b2b2b;
    --sketch: #ddd7c2;
    --daisy: #ffffff;
  }
  * { box-sizing: border-box; margin: 0; padding: 0; }
  html, body {
    width: 900px; height: 1200px; overflow: hidden;
    background: var(--page-bg);
  }
  .canvas { position: relative; width: 900px; height: 1200px; }
  .label {
    position: absolute; left: 100px; top: 22px;
    width: 700px; height: 1156px;
  }
  .label-shape { position: absolute; inset: 0; }
  .label > div { position: absolute; }

  .brand-name {
    left: 0; width: 700px; top: 192px;
    text-align: center;
    font-family: "Montserrat", sans-serif; font-weight: 600;
    font-size: 56px; line-height: 1; letter-spacing: -1px;
    color: var(--ink);
  }
  .title-pure {
    left: 396px; top: 268px;
    font-family: "Shrikhand", serif; font-size: 84px; line-height: 1;
    color: var(--title-brown);
  }
  .title-honey {
    left: 44px; top: 340px;
    font-family: "Shrikhand", serif; font-size: 140px; line-height: 1;
    color: var(--honey-orange);
  }
  .tagline {
    left: 95px; top: 526px;
    font-family: "Gochi Hand", cursive; font-size: 33px; line-height: 1;
    color: var(--ink);
  }
  .farm-scene {
    left: 74px; top: 585px; width: 300px; height: 145px;
    border-radius: 12px;
    background: linear-gradient(180deg, rgba(255,255,255,0) 0%, var(--sketch) 100%);
    opacity: .75;
  }
  .jar-flowers {
    left: 330px; top: 560px; width: 296px; height: 370px;
    border-radius: 40px 40px 90px 90px;
    background: linear-gradient(180deg, var(--honey-light) 0%, var(--honey-deep) 55%, var(--daisy) 100%);
  }
  .packer {
    left: 40px; top: 805px; width: 270px;
    text-align: center;
    font-family: "Montserrat", sans-serif;
  }
  .packer-role {
    font-weight: 700; font-size: 25px; line-height: 1.2;
    color: var(--claim-red);
  }
  .packer-name {
    margin-top: 4px;
    font-weight: 500; font-size: 23px; line-height: 1.25;
    color: var(--farm-green);
  }
  .claims {
    left: 205px; width: 350px; top: 950px;
    display: flex; justify-content: space-between;
  }
  .claim-badge {
    width: 96px; height: 96px; border-radius: 50%;
    background: var(--ink);
    border: 4px solid #ffffff;
    box-shadow: 0 0 0 3px var(--ink);
    display: flex; flex-direction: column; align-items: center; justify-content: center;
    font-family: "Montserrat", sans-serif; color: #ffffff;
    text-align: center;
  }
  .claim-badge .zero { font-size: 12px; font-weight: 700; line-height: 1; }
  .claim-badge .claim-dot {
    width: 26px; height: 26px; border-radius: 50%;
    border: 3px solid #ffffff; margin: 5px 0;
  }
  .claim-badge .claim-word { font-size: 8.5px; font-weight: 600; line-height: 1; }
  .net-weight {
    left: 0; width: 700px; top: 1078px;
    text-align: center;
    font-family: "Montserrat", sans-serif; font-weight: 600;
    font-size: 24px; line-height: 1; color: var(--farm-green);
  }
  .net-weight strong { font-size: 34px; font-weight: 700; margin-left: 6px; }
</style>
</head>
<body>
<div class="canvas">
  <div class="label">
    <svg class="label-shape" width="700" height="1156" viewBox="0 0 700 1156" aria-hidden="true">
      <defs>
        <linearGradient id="label-fill" x1="0" y1="0" x2="0" y2="1">
          <stop offset="0" stop-color="var(--label-cream)"/>
          <stop offset="0.55" stop-color="var(--label-warm)"/>
          <stop offset="1" stop-color="var(--label-cream)"/>
        </linearGradient>
        <linearGradient id="drip-fill" x1="0" y1="0" x2="0" y2="1">
          <stop offset="0" stop-color="var(--honey-gold)"/>
          <stop offset="1" stop-color="var(--honey-light)"/>
        </linearGradient>
        <clipPath id="label-clip">
          <path d="M60,0 H640 Q700,0 700,60 V790 C700,1010 560,1156 350,1156 C140,1156 0,1010 0,790 V60 Q0,0 60,0 Z"/>
        </clipPath>
      </defs>
      <path d="M60,0 H640 Q700,0 700,60 V790 C700,1010 560,1156 350,1156 C140,1156 0,1010 0,790 V60 Q0,0 60,0 Z" fill="url(#label-fill)"/>
      <g clip-path="url(#label-clip)">
        <rect x="0" y="0" width="700" height="165" fill="url(#drip-fill)" role="img" aria-label="Honey dripping down from the top edge over a honeycomb background"/>
      </g>
      <path d="M60,0 H640 Q700,0 700,60 V790 C700,1010 560,1156 350,1156 C140,1156 0,1010 0,790 V60 Q0,0 60,0 Z" fill="none" stroke="var(--border-green)" stroke-width="16"/>
    </svg>

    <div class="brand-name">meadowly</div>
    <div class="title-pure">pure</div>
    <div class="title-honey">Honey</div>
    <div class="tagline">100% Pure &amp; Natural</div>

    <div class="farm-scene" role="img" aria-label="Light line sketch of a farmhouse in rolling hills"></div>
    <div class="jar-flowers" role="img" aria-label="Honey dipper pouring into a glass jar of honey surrounded by white daisies"></div>

    <div class="packer">
      <p class="packer-role">Packed &amp;<br>Distributed by</p>
      <p class="packer-name">Bright Meadow<br>Farms Limited</p>
    </div>

    <div class="claims">
      <div class="claim-badge"><span class="zero">Zero</span><span class="claim-dot"></span><span class="claim-word">Preservatives</span></div>
      <div class="claim-badge"><span class="zero">Zero</span><span class="claim-dot"></span><span class="claim-word">Colouring</span></div>
      <div class="claim-badge"><span class="zero">Zero</span><span class="claim-dot"></span><span class="claim-word">Additive</span></div>
    </div>

    <div class="net-weight">Net WT:<strong>500g</strong></div>
  </div>
</div>
</body>
</html>
```